A4 Flyer

Bright Path Learning is starting a course in regional Victoria. We are currently advertising (See attached file A34984) in local papers but need to create a one page flyer to distribute to Aged Care facilities in the area. The A4 flyer will be inserted into a folder pack with more detailed information on Bright Path Learning. Important to use images and logoes attached

Target Market(s)

Flyer to be distributed to Aged Care facility staff and owners

Industry/Entity Type

Advertising

Font styles to use
Sans Serif

Colors
f37123
ec1f27

Requirements
Must have
• BPL Logo
Some image

```html
<!DOCTYPE html>
<html lang="en">
<head>
<meta charset="utf-8">
<title>Bright Path Learning – Fast Track Course Flyer</title>
<link rel="stylesheet" href="https://fonts.googleapis.com/css2?family=Source+Sans+3:wght@400;600&display=swap">
<style>
  :root {
    --orange: #f37123;
    --orange-light: #f9a03f;
    --red: #ec1f27;
    --red-deep: #d9141c;
    --ink: #3a3a3a;
    --white: #ffffff;
  }
  * { margin: 0; padding: 0; box-sizing: border-box; }
  html, body { width: 849px; height: 1200px; overflow: hidden; background: var(--white); }
  body { font-family: "Source Sans 3", Arial, sans-serif; }
  .flyer { position: relative; width: 849px; height: 1200px; overflow: hidden; background: var(--white); }

  .headline {
    position: absolute; left: 34px; top: 18px;
    color: var(--orange); font-weight: 600; font-size: 78px; line-height: 92px;
    letter-spacing: 0.5px;
  }
  .subhead {
    position: absolute; left: 47px; top: 240px;
    color: var(--red); font-weight: 600; font-size: 29px;
  }

  .brand { position: absolute; left: 612px; top: 22px; width: 200px; text-align: center; }
  .brand-mark { width: 150px; height: 150px; border-radius: 50%; background: var(--orange); margin: 0 auto 18px; }
  .brand-name { color: var(--ink); font-weight: 600; font-size: 34px; line-height: 36px; letter-spacing: 1px; }

  .photo { position: absolute; }
  .photo-trainer { left: 43px; top: 339px; width: 263px; height: 342px;
    background: linear-gradient(160deg, #f1ece8 0%, #e2c9bf 45%, #c95a45 75%, #e9e4e0 100%); }
  .photo-student-a { left: 43px; top: 802px; width: 171px; height: 264px;
    background: linear-gradient(180deg, #f2f0ee 0%, #c9b6a6 40%, #2e2a2c 100%); }
  .photo-student-b { left: 225px; top: 822px; width: 178px; height: 304px;
    background: linear-gradient(180deg, #f1efee 0%, #b79a85 35%, #e8e8ec 100%); }

  .topics {
    position: absolute; left: 316px; top: 339px; width: 489px; height: 342px;
    background: linear-gradient(135deg, var(--orange-light) 0%, var(--orange) 45%, var(--red) 100%);
    color: var(--white); padding: 12px 12px 0 11px;
  }
  .topics-note { font-size: 18.5px; line-height: 25px; }
  .topics-list { list-style: none; margin-top: 4px; }
  .topics-list li { font-size: 24px; line-height: 35px; letter-spacing: 0.5px; }

  .qualification { position: absolute; left: 0; top: 691px; width: 805px; color: var(--white); }
  .qualification-title {
    background: var(--red); height: 40px; text-align: right; padding-right: 20px;
    font-weight: 600; font-size: 28px; line-height: 40px;
  }
  .qualification-name {
    background: var(--red-deep); margin-top: 2px; height: 44px; text-align: center;
    font-size: 23.5px; line-height: 44px; letter-spacing: 0.3px;
  }

  .funding { position: absolute; right: 44px; top: 794px; text-align: right; color: #111; }
  .funding-line { font-size: 24px; line-height: 34px; }
  .funding-fees { font-size: 31px; line-height: 48px; }

  .venue {
    position: absolute; left: 494px; top: 895px; width: 314px; height: 155px;
    background: var(--red); border-radius: 38px; color: var(--white);
    padding: 12px 0 0 32px; font-size: 29px; line-height: 38px;
  }

  .footer-wave { position: absolute; left: 0; top: 1050px; width: 849px; height: 150px; }
  .contact { position: absolute; right: 20px; top: 1118px; text-align: right; color: var(--white); }
  .contact-phone { font-size: 20px; line-height: 30px; letter-spacing: 0.5px; }
  .contact-web { font-size: 28px; line-height: 36px; }
</style>
</head>
<body>
<div class="flyer">
  <h1 class="headline">Unique<br>Opportunity!</h1>
  <p class="subhead">Fast Track Course - Start July 2014</p>

  <div class="brand">
    <div class="brand-mark"></div>
    <div class="brand-name">bright path<br>learning</div>
  </div>

  <div class="photo photo-trainer" role="img" aria-label="Trainer demonstrating on an anatomical torso model"></div>

  <div class="topics">
    <p class="topics-note">This training is delivered with VIC and Comm Govt Funding to eligible students</p>
    <ul class="topics-list">
      <li>Pathology</li>
      <li>Aged Care</li>
      <li>First Aid</li>
      <li>CPR</li>
      <li>Anaphylaxis</li>
      <li>Medications for PCA’s</li>
      <li>Home &amp; Community Care</li>
      <li>Health Services</li>
    </ul>
  </div>

  <div class="qualification">
    <div class="qualification-title">DOUBLE QUALIFICATION</div>
    <div class="qualification-name">CERT III IN AGED CARE WITH HOME AND COMMUNITY CARE</div>
  </div>

  <div class="photo photo-student-a" role="img" aria-label="Student seated at a classroom desk"></div>
  <div class="photo photo-student-b" role="img" aria-label="Student seated at a desk with course papers"></div>

  <div class="funding">
    <p class="funding-line">Government Funding for eligible students!</p>
    <p class="funding-fees">Fees from $117</p>
  </div>

  <div class="venue">Wattle Grove Nursing<br>Home - Stawell<br>9.00am - 3.00pm</div>

  <svg class="footer-wave" viewBox="0 0 849 150" aria-hidden="true">
    <defs>
      <linearGradient id="waveFill" x1="0" y1="0" x2="1" y2="0">
        <stop offset="0" stop-color="#f9a03f"/>
        <stop offset="1" stop-color="#f37123"/>
      </linearGradient>
    </defs>
    <path d="M0 70 C 250 40, 550 0, 849 10 L849 150 L0 150 Z" fill="#fbd3ad"/>
    <path d="M0 85 C 260 55, 560 20, 849 28 L849 150 L0 150 Z" fill="url(#waveFill)"/>
  </svg>

  <div class="contact">
    <p class="contact-phone">CALL 9876 5400</p>
    <p class="contact-web">brightpathlearning.com.au</p>
  </div>
</div>
</body>
</html>
```